Tidal Fern Business Cards

We need something new, fun and exciting for business cards. Our current ones are just plain and we need a design that pops. We want name, position held, phone, email on the front, and a 20% discount on the back. I have also uploaded our old business cards creative to see what we are not wanting, and how boring they were and we want something jazzed up from this, cool design and catches people attention.

```html
<!DOCTYPE html>
<html lang="en">
<head>
<meta charset="UTF-8">
<title>Tidal Fern Business Cards</title>
<link rel="stylesheet" href="https://fonts.googleapis.com/css2?family=Lato:wght@400;700;900&display=swap">
<style>
  :root {
    --navy: #163f6e;
    --coral: #ef6f6c;
    --coral-faint: rgba(239, 111, 108, 0.09);
    --grey: #555a60;
    --paper: #ffffff;
    --stage: #ffffff;
  }
  * { margin: 0; padding: 0; box-sizing: border-box; }
  html, body {
    width: 1200px; height: 656px; overflow: hidden;
    background: var(--stage);
    font-family: "Lato", sans-serif;
  }
  .canvas { position: relative; width: 1200px; height: 656px; }
  .card {
    position: absolute; top: 188px;
    width: 492px; height: 281px;
    background: var(--paper);
    box-shadow: 0 6px 14px rgba(0,0,0,0.28);
    overflow: hidden;
  }
  .card--front { left: 93px; }
  .card--back { left: 602px; }

  .backdrop-disc {
    position: absolute; top: -20px;
    width: 310px; height: 310px; border-radius: 50%;
    background: var(--coral-faint);
  }
  .card--front .backdrop-disc { left: 345px; }
  .card--back .backdrop-disc { left: -164px; }

  .brand {
    position: absolute;
    display: flex; align-items: center; gap: 20px;
    color: var(--navy); font-weight: 900; white-space: nowrap; line-height: 1;
  }
  .brand__dot {
    width: 32px; height: 32px; border-radius: 50%;
    background: var(--coral); flex: none;
  }
  .card--front .brand { left: 30px; top: 34px; font-size: 50px; }
  .card--back .brand { left: 50%; top: 113px; transform: translateX(-50%); font-size: 50px; }

  .person { position: absolute; left: 28px; top: 138px; }
  .person__name {
    color: var(--navy); font-weight: 900; font-size: 23px; letter-spacing: 0.2px; line-height: 1;
  }
  .person__role { color: var(--grey); font-size: 14px; margin-top: 7px; }

  .divider {
    position: absolute; left: 27px; top: 195px;
    width: 438px; height: 1px; background: var(--coral);
  }

  .contacts {
    position: absolute; left: 27px; top: 204px;
    list-style: none; color: var(--grey); font-size: 14px;
  }
  .contacts li { display: flex; align-items: center; gap: 11px; height: 19.5px; }
  .contacts svg { width: 11px; height: 11px; flex: none; }

  .address {
    position: absolute; right: 27px; top: 224px;
    text-align: right; color: var(--grey); font-size: 14px; line-height: 19.5px;
    font-style: normal;
  }

  .offer {
    position: absolute; left: 0; right: 0; top: 232px;
    display: flex; align-items: center; gap: 12px;
  }
  .offer__rule { flex: 1; height: 1px; background: var(--coral); }
  .offer__rule--right { flex: 0 0 171px; }
  .offer__text { color: var(--coral); font-size: 21px; white-space: nowrap; }
</style>
</head>
<body>
<div class="canvas">
  <section class="card card--front">
    <div class="backdrop-disc" aria-hidden="true"></div>
    <div class="brand"><span class="brand__dot"></span>Tidal Fern</div>
    <div class="person">
      <p class="person__name">OWEN HALE</p>
      <p class="person__role">Founder &amp; CEO</p>
    </div>
    <div class="divider"></div>
    <ul class="contacts">
      <li>
        <svg viewBox="0 0 12 12" aria-hidden="true"><path fill="#ef6f6c" d="M2.3 1l2 2.1-1 1.2c.7 1.5 1.9 2.7 3.4 3.4l1.2-1 2.1 2-1.3 1.6C4.9 10.1 1.9 7.1 1.2 3.3z"/></svg>
        1234567890
      </li>
      <li>
        <svg viewBox="0 0 12 12" aria-hidden="true"><rect x="0.5" y="2.5" width="11" height="7.5" fill="#ef6f6c"/><path d="M0.8 2.8L6 7l5.2-4.2M0.8 9.8L4.5 6M11.2 9.8L7.5 6" stroke="#fff" stroke-width="0.8" fill="none"/></svg>
        info@tidalfern.com
      </li>
      <li>
        <svg viewBox="0 0 12 12" aria-hidden="true"><circle cx="6" cy="6" r="5" fill="none" stroke="#ef6f6c" stroke-width="1.2"/><path d="M1 6h10M6 1c-2.4 2.8-2.4 7.2 0 10M6 1c2.4 2.8 2.4 7.2 0 10" stroke="#ef6f6c" stroke-width="0.9" fill="none"/></svg>
        www.tidalfern.com
      </li>
    </ul>
    <address class="address">
      1234 First Line Address<br>
      5678 Second Line Address
    </address>
  </section>

  <section class="card card--back">
    <div class="backdrop-disc" aria-hidden="true"></div>
    <div class="brand"><span class="brand__dot"></span>Tidal Fern</div>
    <div class="offer">
      <span class="offer__rule"></span>
      <span class="offer__text">20% discount</span>
      <span class="offer__rule offer__rule--right"></span>
    </div>
  </section>
</div>
</body>
</html>
```